Real Estate Superstar Business Card Design

We need a business card design for a new superstar real estate sales team based out of the Greater Toronto Area. A bit about us: The Agent in charge is Derek Osmond. We are a hard working team that heavily depends on our defined knowledge, aggressive skills and strong attitude to continue delivering exceptional service with amazing results for buyers and sellers.

Information that should be included on the card:
NestPoint Summit Realty Inc. ,Brokerage
4163 Bellowind Rd. #17
Mississauga, ON K7T 2M4
Independently Owned & Operated

Dir: 647-381-4062
Off: 905-716-3048
Fax: 905-716-3041

Industry/Entity Type

Real Estate

Font styles to use
Script

Requirements
Must have
• -NestPoint Summit Logo
-Derek Osmond Logo

```html
<!DOCTYPE html>
<html lang="en">
<head>
<meta charset="utf-8">
<title>Derek Osmond – Business Card</title>
<link href="https://fonts.googleapis.com/css2?family=Tinos:wght@400;700&display=swap" rel="stylesheet">
<style>
  :root {
    --card-bg: #e7e8ea;
    --navy: #1d2559;
    --text-grey: #58595b;
    --title-grey: #707174;
    --frame-red: #e0343c;
    --frame-blue: #2fb2e6;
    --badge-gold: #e7b632;
    --suit-dark: #2f3236;
    --suit-mid: #6a6e74;
    --shirt-light: #dfe4ea;
  }
  html, body {
    margin: 0;
    padding: 0;
    overflow: hidden;
    background: #ffffff;
  }
  .card {
    position: relative;
    width: 1200px;
    height: 716px;
    background: var(--card-bg);
    overflow: hidden;
    font-family: "Tinos", "Times New Roman", serif;
  }
  .portrait {
    position: absolute;
    left: 0;
    top: 0;
    width: 338px;
    height: 716px;
    background: linear-gradient(100deg, var(--suit-dark) 0%, var(--suit-mid) 45%, var(--shirt-light) 80%, var(--card-bg) 100%);
  }
  .frame-outer {
    position: absolute;
    left: 7px; top: 7px; right: 7px; bottom: 7px;
    border: 1.5px solid var(--frame-red);
  }
  .frame-inner {
    position: absolute;
    left: 24px; top: 24px; right: 24px; bottom: 24px;
    border: 1.5px solid var(--frame-blue);
  }
  .monogram {
    position: absolute;
    left: 517px;
    top: 60px;
    width: 160px;
    text-align: center;
    font-size: 130px;
    font-weight: 700;
    line-height: 1;
    color: var(--navy);
  }
  .agent-name {
    position: absolute;
    left: 410px;
    top: 232px;
    margin: 0;
    font-size: 52px;
    font-weight: 700;
    letter-spacing: 3px;
    line-height: 1;
    color: var(--navy);
  }
  .agent-title {
    position: absolute;
    left: 415px;
    top: 282px;
    margin: 0;
    font-size: 30px;
    font-weight: 700;
    letter-spacing: 1px;
    line-height: 1;
    color: var(--title-grey);
  }
  .title-rule {
    position: absolute;
    left: 388px;
    top: 315px;
    width: 428px;
    height: 4px;
    background: var(--navy);
  }
  .phones, .online, .office {
    position: absolute;
    left: 410px;
    margin: 0;
    font-weight: 700;
    color: var(--text-grey);
  }
  .phones { top: 343px; font-size: 30px; line-height: 34px; }
  .online { top: 480px; font-size: 30px; line-height: 31px; }
  .office { top: 544px; font-size: 20px; line-height: 29.5px; }
  .phones span, .online span, .office span { display: block; }
  .brokerage-mark {
    position: absolute;
    left: 952px;
    top: 470px;
    width: 150px;
    text-align: center;
  }
  .brokerage-mark svg { display: block; margin: 0 auto 10px; }
  .brokerage-name {
    font-size: 24px;
    font-weight: 700;
    color: var(--navy);
    line-height: 1;
  }
</style>
</head>
<body>
<div class="card">
  <div class="portrait" role="img" aria-label="Portrait photo of the agent in a dark suit and blue tie"></div>
  <div class="frame-outer"></div>
  <div class="frame-inner"></div>

  <div class="monogram">DO</div>

  <h1 class="agent-name">Derek Osmond</h1>
  <p class="agent-title">Real Esate Consultant</p>
  <div class="title-rule"></div>

  <p class="phones">
    <span>Dir: 647-381-4062</span>
    <span>Off: 905-716-3048</span>
    <span>Fax: 905-716-3041</span>
  </p>

  <p class="online">
    <span>Derek@summitnestgta.com</span>
    <span>www.summitnestgta.com</span>
  </p>

  <p class="office">
    <span>NestPoint Summit Realty Inc. ,Brokerage</span>
    <span>4163 Bellowind Rd. #17</span>
    <span>Mississauga, ON K7T 2M4</span>
    <span>Independently Owned &amp; Operated</span>
  </p>

  <div class="brokerage-mark">
    <svg width="100" height="100" viewBox="0 0 100 100" aria-hidden="true">
      <circle cx="50" cy="50" r="46" fill="none" stroke="var(--badge-gold)" stroke-width="6"/>
    </svg>
    <div class="brokerage-name">NestPoint</div>
  </div>
</div>
</body>
</html>
```